Book cover for my book "Gentle Uncoupling"

Simple graphic with the title "Gentle Uncoupling" for a book I am self publishing. This book teaches people how to divorce with kindness and compassion without compromising their legal rights and getting what is fair. I am a lawyer telling them everything on how to hire a lawyer, what process to choose, how to build a support system, how to keep the kids out of it. It should exude authority, but also kindness and compassion. It's real legal information but from a lens that doesn't give a bunch of money to lawyers to burn down your family.

Target Market(s)

People seeking to divorce but don't want to spend a bunch of money or destroy their spouse

Industry/Entity Type

Legal

Requirements
Must have
• Dignity
Nice to have
• Envision two people parting, moving away from each other but something that is altruistic popping up between them? I'm not artist. Keep in mind "couple" is generic so not gender specific.
Should not have
• Trite things like a handshake,

```html
<!DOCTYPE html>
<html lang="en">
<head>
<meta charset="utf-8">
<title>Gentle Uncoupling – Cover Options</title>
<link rel="stylesheet" href="https://fonts.googleapis.com/css2?family=Pinyon+Script&family=Cinzel:wght@400;600&display=swap">
<style>
  :root {
    --stage: #000000;
    --paper: #ffffff;
    --maroon: #8a1c22;
    --ink: #111111;
    --sky-light: #7ac8ee;
    --sky-mid: #3a8fc4;
    --deep: #13222e;
    --rose: #c48a8e;
    --grad-top: #8b1a1f;
    --grad-plum: #5a3f5e;
    --grad-steel: #3a6e9e;
    --grad-cyan: #0b96d9;
  }
  * { margin: 0; padding: 0; box-sizing: border-box; }
  html, body {
    width: 1200px; height: 738px; overflow: hidden;
    background: var(--stage);
  }
  .stage { position: relative; width: 1200px; height: 738px; }

  .cover {
    position: absolute; top: 46px;
    width: 419px; height: 644px;
    overflow: hidden;
  }
  .cover--light { left: 112px; background: var(--paper); }
  .cover--gradient {
    left: 669px;
    background: linear-gradient(180deg,
      var(--grad-top) 0%, var(--grad-plum) 30%, var(--grad-steel) 55%,
      var(--grad-cyan) 80%, var(--paper) 100%);
  }

  .figure {
    position: absolute;
    background: linear-gradient(90deg,
      var(--sky-light) 0%, var(--sky-mid) 25%, var(--deep) 60%, var(--rose) 100%);
    opacity: 0.92;
  }
  .figure--left  { left: 0;     top: 203px; width: 175px; height: 441px; border-radius: 0 70px 0 0; }
  .figure--right { left: 242px; top: 187px; width: 177px; height: 457px; border-radius: 70px 0 0 0; }

  .title-script {
    position: absolute; top: 80px; left: 0; width: 100%;
    text-align: center;
    font-family: "Pinyon Script", cursive;
    font-size: 66px; line-height: 1;
  }
  .cover--light .title-script { color: var(--ink); }
  .cover--gradient .title-script { color: var(--paper); }

  .title-stack {
    position: absolute; top: 172px; left: 50%;
    transform: translateX(-50%);
    display: flex; flex-direction: column; align-items: center;
    font-family: "Cinzel", serif;
    font-size: 29px; line-height: 38px;
  }
  .cover--light .title-stack { color: var(--maroon); }
  .cover--gradient .title-stack { color: var(--paper); }

  .imprint {
    position: absolute; top: 597px; left: 50%;
    transform: translateX(-50%);
    display: flex; align-items: center; gap: 6px;
    white-space: nowrap;
    font-family: "Cinzel", serif; font-weight: 600;
    font-size: 10px; letter-spacing: 0.5px;
    color: var(--maroon);
  }
  .imprint__dot {
    width: 14px; height: 14px; border-radius: 50%;
    background: var(--maroon);
  }
</style>
</head>
<body>
<main class="stage">

  <section class="cover cover--light">
    <div class="figure figure--left" role="img" aria-label="Abstract layered figure in blue and rose tones, one partner turning away"></div>
    <div class="figure figure--right" role="img" aria-label="Abstract layered figure in blue and rose tones, the other partner turning away"></div>
    <h1 class="title-script">Gentle</h1>
    <div class="title-stack" aria-label="Uncoupling">
      <span>U</span><span>N</span><span>C</span><span>O</span><span>U</span><span>P</span><span>L</span><span>I</span><span>N</span><span>G</span>
    </div>
    <div class="imprint"><span class="imprint__dot"></span>The Kindred Counsel</div>
  </section>

  <section class="cover cover--gradient">
    <div class="figure figure--left" role="img" aria-label="Abstract layered figure in blue and rose tones, one partner turning away"></div>
    <div class="figure figure--right" role="img" aria-label="Abstract layered figure in blue and rose tones, the other partner turning away"></div>
    <h1 class="title-script">Gentle</h1>
    <div class="title-stack" aria-label="Uncoupling">
      <span>U</span><span>N</span><span>C</span><span>O</span><span>U</span><span>P</span><span>L</span><span>I</span><span>N</span><span>G</span>
    </div>
    <div class="imprint"><span class="imprint__dot"></span>The Kindred Counsel</div>
  </section>

</main>
</body>
</html>
```